Postcard: Open Sky Circle

Text for front: HOW TO CHANGE THE WORLD IN ONE [note: the word "one" should be underlined] STEPHint: It's up to you...[Note: add arrow or something to indicate "turn over"]Text for back: You're going to spend your entire life with someone you can never get away from. (Guess who?) Wouldn't you rather that person #OpenSkyCircle than judgmental or critical? BE the change you want to see! Visit www.OpenSkyCircle-hub.example for daily Dawn Pebbles and community. PLEASE JOIN US![Note: add logo to left half of back side]Font preference for text: Josefin sans

Target Market(s)

People who would be attracted to Corvane church - teravian perennist message. It's spiritual without being overtly religious, so the target market is probably early 30s and up but ideally won't turn off Millennials (folks under 30). It should attract attention of people who are open-minded and committed to progressive social change, tired of an atmosphere of hate-mongering and divisiveness.

Requirements
Nice to have
• It would be nice to convey a sense of challenge - there is an idea of "dawn pebbles" so something related to fire/sparks is appropriate. This is meant to evoke a deeper, divine love more than a sense of romantic love. This love is more fierce than fluffy! Yet it calls us to be our best selves.
Should not have
• Please avoid excessive pink - just the logo is enough, as this design needs to appeal to men as well as women.

```html
<!DOCTYPE html>
<html lang="en">
<head>
<meta charset="utf-8">
<title>Open Sky Circle – Postcard</title>
<link rel="stylesheet" href="https://fonts.googleapis.com/css2?family=Cinzel:wght@400&family=Cormorant+Garamond:wght@500&family=Arimo:wght@400;700&display=swap">
<style>
  :root {
    --backdrop: #a9a7a8;
    --card: #ffffff;
    --rose-band: #e4446e;
    --rose-deep: #e81d55;
    --rose-text: #e0356a;
    --rose-soft: #f3a3bb;
    --url-red: #e8103f;
    --white: #ffffff;
  }
  * { margin: 0; padding: 0; box-sizing: border-box; }
  html, body {
    width: 862px;
    height: 1200px;
    overflow: hidden;
    background: var(--backdrop);
  }
  .canvas { position: relative; width: 862px; height: 1200px; }

  .card {
    position: absolute;
    background: var(--card);
    overflow: hidden;
  }

  /* Front */
  .card--front { left: 34px; top: 35px; width: 791px; height: 562px; }
  .brand-mark {
    position: absolute;
    left: 0; right: 0; top: 60px;
    display: flex;
    flex-direction: column;
    align-items: center;
    gap: 12px;
  }
  .brand-mark__dot {
    width: 58px; height: 58px;
    border-radius: 50%;
    background: var(--rose-soft);
  }
  .brand-mark__name {
    font-family: "Cinzel", serif;
    font-size: 22px;
    letter-spacing: 3px;
    color: var(--rose-text);
  }
  .title-band {
    position: absolute;
    left: 0; top: 228px;
    width: 100%; height: 258px;
    background: var(--rose-band);
    color: var(--white);
    font-family: "Cinzel", serif;
    font-size: 62px;
    letter-spacing: 4px;
    text-align: center;
  }
  .title-band__line {
    position: absolute;
    left: 0; right: 0;
    line-height: 1;
  }
  .title-band__line--1 { top: 20px; }
  .title-band__line--2 { top: 102px; }
  .title-band__line--3 { top: 186px; }
  .title-band__highlight {
    display: inline-block;
    background: var(--white);
    color: var(--rose-band);
    padding: 6px 6px 4px;
    margin: -6px 6px 0 0;
  }
  .hint {
    position: absolute;
    left: 201px; top: 505px;
    font-family: "Cormorant Garamond", serif;
    font-weight: 500;
    font-size: 32px;
    letter-spacing: 3px;
    color: var(--rose-text);
    line-height: 1;
  }
  .turn-arrows {
    position: absolute;
    left: 559px; top: 510px;
    width: 191px; height: 32px;
  }

  /* Back */
  .card--back { left: 34px; top: 616px; width: 787px; height: 561px; }
  .rule {
    position: absolute;
    left: 0; width: 100%;
    background: var(--rose-deep);
  }
  .rule--top { top: 48px; height: 5px; }
  .rule--bottom { top: 262px; height: 6px; }
  .message-band {
    position: absolute;
    left: 0; top: 62px;
    width: 100%; height: 193px;
    background: var(--rose-deep);
    color: var(--white);
    font-family: "Arimo", sans-serif;
    font-size: 26px;
    line-height: 44.5px;
    text-align: center;
    padding-top: 11px;
  }
  .back-copy {
    position: absolute;
    left: 0; right: 0;
    font-family: "Arimo", sans-serif;
    color: var(--rose-text);
    text-align: center;
    line-height: 1;
  }
  .back-copy--change { top: 278px; font-size: 26px; left: -30px; }
  .back-mark {
    position: absolute;
    left: 0; right: 0; top: 336px;
    display: flex;
    flex-direction: column;
    align-items: center;
    gap: 6px;
  }
  .back-mark__dot {
    width: 34px; height: 34px;
    border-radius: 50%;
    background: var(--rose-soft);
  }
  .back-mark__name {
    font-family: "Arimo", sans-serif;
    font-size: 18px;
    color: var(--rose-text);
  }
  .back-copy--invite { top: 415px; font-size: 26px; left: -10px; }
  .back-copy--join { top: 459px; font-size: 26px; left: -20px; }
  .back-copy--url {
    top: 506px;
    font-size: 25px;
    font-weight: 700;
    color: var(--url-red);
    text-shadow: 1px 2px 3px rgba(0,0,0,0.35);
    left: -20px;
  }
</style>
</head>
<body>
<main class="canvas">

  <section class="card card--front" aria-label="Postcard front">
    <div class="brand-mark">
      <span class="brand-mark__dot" aria-hidden="true"></span>
      <span class="brand-mark__name">Open Sky Circle</span>
    </div>

    <h1 class="title-band">
      <span class="title-band__line title-band__line--1">HOW TO CHANGE</span>
      <span class="title-band__line title-band__line--2">THE WORLD</span>
      <span class="title-band__line title-band__line--3">IN <span class="title-band__highlight">ONE</span>STEP</span>
    </h1>

    <p class="hint">Hint: It's up to you...</p>

    <svg class="turn-arrows" viewBox="0 0 191 32" aria-label="Turn over">
      <g fill="#e4446e">
        <polygon points="0,0 9,0 22,16 9,32 0,32 13,16"/>
        <polygon points="21,0 30,0 43,16 30,32 21,32 34,16"/>
        <polygon points="42,0 51,0 64,16 51,32 42,32 55,16"/>
        <polygon points="63,0 72,0 85,16 72,32 63,32 76,16"/>
        <polygon points="84,0 93,0 106,16 93,32 84,32 97,16"/>
        <polygon points="105,0 114,0 127,16 114,32 105,32 118,16"/>
        <polygon points="126,0 135,0 148,16 135,32 126,32 139,16"/>
        <polygon points="147,0 156,0 169,16 156,32 147,32 160,16"/>
        <polygon points="168,0 177,0 190,16 177,32 168,32 181,16"/>
      </g>
    </svg>
  </section>

  <section class="card card--back" aria-label="Postcard back">
    <div class="rule rule--top"></div>
    <div class="message-band">
      <p>You're going to spend your entire life with someone you can<br>
      never get away from. (Guess who?)<br>
      Wouldn't you rather that person<br>
      #OpenSkyCircle than judgmental or critical?</p>
    </div>
    <div class="rule rule--bottom"></div>

    <p class="back-copy back-copy--change">BE the change you want to see!</p>

    <div class="back-mark">
      <span class="back-mark__dot" aria-hidden="true"></span>
      <span class="back-mark__name">Open Sky Circle</span>
    </div>

    <p class="back-copy back-copy--invite">For daily Dawn Pebbles and community.</p>
    <p class="back-copy back-copy--join">PLEASE JOIN US!</p>
    <p class="back-copy back-copy--url">www.OpenSkyCircle-hub.example</p>
  </section>

</main>
</body>
</html>
```